A new novel about the early days of The Marlows needs a book cover design

The title of the book is A LANTERN IN WINTER
The cover should also include "a novel" and "by Tom Holloway" Those can be together or separate.
The design element I'd like to incorporate is the iconic "Dock Wall" photo of The Marlows in 1960, which I've attached below. Since we're not sure if we can get the rights to the actual photo, it's probably best if the design merely references that photo, or distorts it in an interesting way. But it should be very clear that the book is about the Marlows.
The novel is in many ways based on that photo and evokes the city of Hamburg in 1960, which was gritty, raw, and sexually charged (as were The Marlows).
The tone of the novel is romantic, passionate, and very funny - but never broad and silly.

```html
<!DOCTYPE html>
<html lang="en">
<head>
<meta charset="utf-8">
<title>A Lantern in Winter — Tom Holloway</title>
<link rel="stylesheet" href="https://fonts.googleapis.com/css2?family=Montserrat:wght@300&family=Oswald:wght@500&display=swap">
<style>
  :root {
    --cover-bg: #1b1c19;
    --ink-light: #d9dbd6;
    --title-ink: #cbcdc8;
    --scene-light: #e0e1de;
    --scene-dark: #2a2b27;
  }
  html, body {
    margin: 0;
    padding: 0;
    overflow: hidden;
    background: var(--cover-bg);
  }
  .cover {
    position: relative;
    width: 750px;
    height: 1200px;
    overflow: hidden;
    background: var(--cover-bg);
  }
  .byline {
    position: absolute;
    left: 0;
    width: 100%;
    text-align: center;
    margin: 0;
    color: var(--ink-light);
    font-family: "Montserrat", sans-serif;
    font-weight: 300;
    line-height: 1;
  }
  .byline-kicker {
    top: 58px;
    font-size: 31px;
    letter-spacing: 1px;
  }
  .byline-author {
    top: 134px;
    font-size: 47px;
    letter-spacing: 2px;
  }
  .band-scene {
    position: absolute;
    left: 0;
    top: 236px;
    width: 750px;
    height: 300px;
  }
  .band-scene .window-light { fill: var(--scene-light); }
  .band-scene .window-frame { fill: var(--cover-bg); }
  .band-scene .band-figures { fill: var(--scene-dark); }
  .title {
    position: absolute;
    left: 0;
    top: 0;
    width: 750px;
    height: 1200px;
  }
  .title text {
    fill: var(--title-ink);
    font-family: "Oswald", sans-serif;
    font-weight: 500;
  }
</style>
</head>
<body>
  <main class="cover">
    <p class="byline byline-kicker">a novel by</p>
    <p class="byline byline-author">TOM HOLLOWAY</p>

    <svg class="band-scene" viewBox="0 0 750 300" role="img" aria-label="Stylised high-contrast illustration of The Marlows: five young musicians in dark jackets, seated with guitars and a drum before a bank of bright windows, Hamburg 1960">
      <rect class="window-light" x="0" y="4" width="750" height="158"/>
      <rect class="window-frame" x="0" y="14" width="750" height="8"/>
      <rect class="window-frame" x="84" y="14" width="10" height="150"/>
      <rect class="window-frame" x="176" y="14" width="10" height="150"/>
      <rect class="window-frame" x="354" y="14" width="10" height="150"/>
      <rect class="window-frame" x="578" y="14" width="10" height="150"/>
      <rect class="window-frame" x="718" y="14" width="10" height="150"/>
      <rect class="band-figures" x="0" y="160" width="750" height="140"/>
    </svg>

    <svg class="title" viewBox="0 0 750 1200" role="heading" aria-level="1" aria-label="A Lantern in Winter">
      <text class="title-small" x="455" y="680" font-size="170" text-anchor="middle">A</text>
      <text class="title-main" x="88" y="962" font-size="330" textLength="577" lengthAdjust="spacingAndGlyphs">LANTERN</text>
      <text class="title-sub" x="95" y="1155" font-size="175" textLength="575" lengthAdjust="spacingAndGlyphs">IN WINTER</text>
    </svg>
  </main>
</body>
</html>
```